Business Card Design Project

I need a business card design for an Organic drive thru coffee kiosk. We will serve organic coffee, teas & smoothies and will serve healthy breakfast food/snacks for people on the go.
I want the card to have 2-3 colors max (earthy colors like browns, greens and so on).
I have attached the logo I want used and would love to play off the theme of "balance."
Include:
Tidy-Kettle Coffee
address: 4820 Gorvin Ct. Raleigh, NC 27583
phone: 919-731-4062
website: www.tidy-kettle.com (website is not up yet but still include it on card)
email: Rosalind@tidy-kettle.com
I want one of the following sayings somewhere on the card (the front or back is fine):
"Eat & Drink Well, on the run!"
"Break the fast with Tidy-Kettle"
Maybe on the back list what we offer:
-Organic coffee, espresso & tea
-Blendora smoothies & protein shakes
-Zesty Pour (100% fresh local fruit and veggies)
-Tender Nibs

```html
<!DOCTYPE html>
<html lang="en">
<head>
<meta charset="utf-8">
<title>Tidy-Kettle Coffee – Business Card</title>
<link rel="stylesheet" href="https://fonts.googleapis.com/css2?family=Andika:wght@400;700&family=Open+Sans:wght@600&display=swap">
<style>
  :root {
    --backdrop: #5b3222;
    --green-light: #93c850;
    --green: #77ad3c;
    --green-text: #8dc63f;
    --brown: #4a2a1a;
    --brown-mid: #7a3f28;
    --rust: #8a3b25;
    --panel-dark: #2f1a12;
    --panel-glow: #4b3024;
  }
  * { margin: 0; padding: 0; box-sizing: border-box; }
  html, body { width: 1200px; height: 1181px; overflow: hidden; }
  body {
    position: relative;
    background: var(--backdrop);
    font-family: "Andika", sans-serif;
  }
  .card {
    position: absolute;
    left: 221px;
    width: 757px;
    height: 436px;
    border-radius: 28px;
    overflow: hidden;
  }
  .card-front {
    top: 125px;
    background: radial-gradient(ellipse at 50% 45%, var(--green-light) 0%, var(--green) 75%);
  }
  .brand-dot {
    position: absolute;
    left: 343px; top: 135px;
    width: 70px; height: 70px;
    border-radius: 50%;
    background: var(--brown-mid);
  }
  .brand-name {
    position: absolute;
    left: 0; right: 0; top: 212px;
    text-align: center;
    font-weight: 700;
    font-size: 62px;
    line-height: 1;
    color: var(--brown);
  }
  .brand-tagline {
    position: absolute;
    left: 0; right: 0; top: 290px;
    text-align: center;
    font-family: "Open Sans", sans-serif;
    font-weight: 600;
    font-size: 13.5px;
    letter-spacing: 2.6px;
    color: var(--rust);
  }
  .front-web {
    position: absolute;
    left: 0; right: 0; bottom: 12px;
    text-align: center;
    font-size: 15px;
    color: var(--brown);
  }
  .bullet-dot {
    display: inline-block;
    width: 11px; height: 11px;
    border-radius: 50%;
    background: var(--brown-mid);
    vertical-align: -1px;
    margin: 0 5px;
  }
  .card-back { top: 612px; background: var(--green); }
  .band {
    position: absolute; left: 0; right: 0;
    display: flex; align-items: center; justify-content: center;
    font-size: 16px; color: var(--brown);
  }
  .band-top { top: 0; height: 66px; }
  .band-bottom { bottom: 0; height: 65px; }
  .band .bullet-dot { width: 15px; height: 15px; vertical-align: -3px; }
  .panel {
    position: absolute; left: 0; right: 0; top: 66px; height: 305px;
    background: radial-gradient(ellipse at 50% 40%, var(--panel-glow) 0%, var(--panel-dark) 80%);
    color: var(--green-text);
  }
  .panel-circle {
    position: absolute; top: 87px;
    width: 90px; height: 130px;
    border-radius: 50%;
    background: var(--brown-mid);
  }
  .panel-circle.left { left: 29px; }
  .panel-circle.right { right: 29px; }
  .services {
    position: absolute; left: 177px; top: 100px;
    list-style: none;
    font-size: 16px; line-height: 21.3px;
  }
  .services-title::before {
    content: ""; display: inline-block;
    width: 6px; height: 6px; background: var(--green-text);
    margin: 0 7px 3px 0;
  }
  .contact {
    position: absolute; left: 0; right: 0; top: 258px;
    text-align: center; font-size: 15px; line-height: 21px;
  }
</style>
</head>
<body>
  <section class="card card-front">
    <div class="brand-dot"></div>
    <div class="brand-name">Tidy-Kettle</div>
    <div class="brand-tagline">ORGANIC COFFEE + CAFE</div>
    <div class="front-web"><span class="bullet-dot"></span>www.tidy-kettle.com<span class="bullet-dot"></span></div>
  </section>

  <section class="card card-back">
    <div class="band band-top"><span class="bullet-dot"></span>Break the fast with Tidy-Kettle<span class="bullet-dot"></span></div>
    <div class="panel">
      <div class="panel-circle left"></div>
      <div class="panel-circle right"></div>
      <ul class="services">
        <li class="services-title">Services we offer :</li>
        <li>- Organic coffee, espresso &amp; tea</li>
        <li>- Blendora smoothies &amp; protein shakes</li>
        <li>- Zesty Pour (100% fresh local fruit and veggies)</li>
        <li>- Tender Nibs</li>
      </ul>
      <div class="contact">
        4820 Gorvin Ct. Raleigh, NC 27583<br>
        919-731-4062 | Rosalind@tidy-kettle.com
      </div>
    </div>
    <div class="band band-bottom"><span class="bullet-dot"></span>Eat &amp; Drink Well, on the run!<span class="bullet-dot"></span></div>
  </section>
</body>
</html>
```